Refer a Friend A5 Flyer for Healthcare Staff

We need an A5 flyer that we can hand out to existing and new staff members promoting our Refer a friend Scheme. We need the leaflet to encourage staff to talk to their family and friends about joining our Healthcare Agency, which provides staff to local care related establishments. Using our logo and brand colours blue and green, as per our website, the final design will need to clearly convey the benefits and attractions of referring additional staff to the team. In addition is the promotion of our Friendloop page, requesting staff to like the page and to like and share various posts.

Target Market(s)

Healthcare and potential Healthcare Staff

Industry/Entity Type

Healthcare

Colors
33b8a4
3277b5

Requirements
Must have
• Company Logo, Brand colours,
• text; "Refer a Friend and receive a £50 Bonus after just 1 completed shift"
• text; "3 easy steps to refer a friend, 1 Fill out your name on the back of your Business Card 2 Hand the card to your friend or any person you wish to refer, 3 ask your friend to present the card to us when they attend their interview"
• text; "Like and share any of our Open Days on Friendloop for a chance to win a prize, you can find us easily by searching @CarewellPlacementGroup"
• text; "Like our Page to stay up to date with our events and offers"
Nice to have
• care worker / elderly care / support worker pictures
• Content / pics from website www.carewellplacementgroup.co.uk

```html
<!DOCTYPE html>
<html lang="en">
<head>
<meta charset="utf-8">
<title>Refer a Friend – Carewell Placement Group</title>
<link href="https://fonts.googleapis.com/css2?family=Jost:wght@500;600&family=Questrial&display=swap" rel="stylesheet">
<style>
  :root {
    --brand-blue: #3277b5;
    --brand-green: #33b8a4;
    --band-green: rgba(108, 196, 176, 0.95);
    --overlay-blue: rgba(110, 150, 205, 0.72);
    --paper: #ffffff;
  }
  * { margin: 0; padding: 0; box-sizing: border-box; }
  html, body { width: 846px; height: 1200px; overflow: hidden; background: var(--paper); }
  .flyer {
    position: relative;
    width: 846px;
    height: 1200px;
    background: var(--paper);
    font-family: "Jost", "Century Gothic", sans-serif;
    color: var(--brand-blue);
  }
  .brand {
    position: absolute;
    top: 52px;
    left: 0;
    width: 100%;
    display: flex;
    justify-content: center;
    align-items: center;
    gap: 12px;
  }
  .brand-dot {
    width: 30px; height: 30px;
    border-radius: 50%;
    background: var(--brand-green);
  }
  .brand-name {
    font-weight: 500;
    font-size: 30px;
    color: var(--brand-blue);
  }
  .headline {
    position: absolute;
    top: 174px;
    left: 0;
    width: 100%;
    text-align: center;
    font-weight: 600;
    font-size: 48.5px;
    line-height: 50px;
    color: var(--brand-blue);
  }
  .hero {
    position: absolute;
    top: 289px;
    left: 0;
    width: 846px;
    height: 670px;
    background:
      linear-gradient(90deg, rgba(240,235,225,0.9) 0%, rgba(220,190,150,0) 18%, rgba(0,0,0,0) 70%, rgba(235,240,245,0.9) 100%),
      linear-gradient(180deg, #cfa46a 0%, #d9b98c 35%, #c9b2a2 60%, #b9b4b8 100%);
  }
  .steps-band {
    position: absolute;
    top: 666px;
    left: 0;
    width: 846px;
    height: 59px;
    background: var(--band-green);
    color: var(--paper);
    font-weight: 600;
    font-size: 47px;
    line-height: 59px;
    text-align: center;
  }
  .steps-panel {
    position: absolute;
    top: 725px;
    left: 0;
    width: 846px;
    height: 234px;
    background: var(--overlay-blue);
  }
  .step {
    position: absolute;
    top: 738px;
    width: 214px;
    height: 214px;
    border-radius: 50%;
    background: var(--brand-blue);
    color: var(--paper);
    text-align: center;
    font-weight: 500;
    font-size: 22px;
    line-height: 27px;
    letter-spacing: 0.3px;
  }
  .step-number { display: block; margin-top: 10px; font-size: 21px; }
  .step-text { display: block; margin-top: 20px; }
  .step--one { left: 44px; }
  .step--two { left: 316px; }
  .step--three { left: 587px; }
  .step--three .step-text { margin-top: 7px; }
  .social-note {
    position: absolute;
    top: 974px;
    left: 0;
    width: 100%;
    text-align: center;
    font-weight: 500;
    font-size: 27.5px;
    line-height: 32.5px;
    color: var(--brand-green);
  }
  .page-note {
    position: absolute;
    top: 1086px;
    left: 0;
    width: 100%;
    text-align: center;
    font-weight: 500;
    font-size: 27.5px;
    line-height: 32px;
    color: var(--brand-blue);
  }
  .site-url {
    position: absolute;
    top: 1141px;
    left: 0;
    width: 100%;
    text-align: center;
    font-family: "Questrial", "Century Gothic", sans-serif;
    font-size: 22px;
    color: var(--brand-blue);
  }
</style>
</head>
<body>
  <main class="flyer">
    <header class="brand">
      <span class="brand-dot"></span>
      <span class="brand-name">Carewell Placement Group</span>
    </header>

    <h1 class="headline">Refer a Friend and receive a £50<br>Bonus after just 1 completed shift</h1>

    <div class="hero" role="img" aria-label="Photo of a smiling elderly woman walking arm in arm with a care worker in a white uniform along a bright corridor"></div>

    <h2 class="steps-band">3 easy steps to refer a friend</h2>
    <div class="steps-panel"></div>

    <div class="step step--one">
      <span class="step-number">1</span>
      <span class="step-text">Fill out your<br>name on the<br>back of your<br>Business Card</span>
    </div>
    <div class="step step--two">
      <span class="step-number">2</span>
      <span class="step-text">Hand the card<br>to your friend or<br>any person you<br>wish to refer</span>
    </div>
    <div class="step step--three">
      <span class="step-number">3</span>
      <span class="step-text">Ask your friend<br>to present the<br>card to us when<br>they attend their<br>interview</span>
    </div>

    <p class="social-note">Like and share any of our Open Days on Friendloop for<br>a chance to win a prize, you can find us easily by<br>searching @CarewellPlacementGroup</p>

    <p class="page-note">Like our Page to stay up to date with our events and offers</p>

    <p class="site-url">www.carewellplacementgroup.co.uk</p>
  </main>
</body>
</html>
```